Brightnest Stays Stationery Design

Letterpaper, business cards, notebook, envelope A4 & A5

Target Market(s)

Business, accommodation, hotels, flexible housing

Font styles to use
Other font styles liked:
• Montserrat

Colors

Designer to choose only greyscale colors for use in the design.

Requirements
Must have
• Luxurious appearance
Keep it simple, just like the logo
Modern
Nice to have
• Tight Luxury Design
Should not have
• Illustrations
Decorative

```html
<!DOCTYPE html>
<html lang="en">
<head>
<meta charset="utf-8">
<title>Brightnest Stays Stationery</title>
<link href="https://fonts.googleapis.com/css2?family=Montserrat:wght@400;600&family=Lato:wght@300;400;700&family=Pinyon+Script&display=swap" rel="stylesheet">
<style>
  :root{
    --backdrop:#cdcdcd;
    --paper:#ebebeb;
    --ink:#231f20;
    --text:#3a3a3a;
    --muted:#6d6d6d;
    --rule:#bdbdbd;
    --white:#f4f4f4;
  }
  *{margin:0;padding:0;box-sizing:border-box}
  html,body{width:1200px;height:857px;overflow:hidden;background:var(--backdrop)}
  .canvas{position:relative;width:1200px;height:857px}
  .sheet{position:absolute;overflow:hidden}
  .paper{background:var(--paper)}
  .dark{background:var(--ink)}
  .base-band{position:absolute;left:0;bottom:0;width:100%;background:var(--ink);border-top:1px solid var(--rule)}
  .brand-mark{font-family:"Montserrat",sans-serif;font-weight:400;text-transform:uppercase;
    letter-spacing:.14em;line-height:1.25;text-align:center;color:var(--ink);position:absolute}
  .brand-mark.on-dark{color:var(--white)}
  .brand-mark span{display:block}
  .contact{position:absolute;font-family:"Montserrat",sans-serif;color:var(--muted)}
  .contact p{white-space:nowrap}
  .contact .icon{display:inline-block;width:1em;height:1em;vertical-align:-.12em;margin-right:.35em;fill:var(--muted)}

  /* letterhead */
  .letterhead{left:120px;top:185px;width:391px;height:553px;box-shadow:2px 3px 6px rgba(0,0,0,.18)}
  .letterhead .brand-mark{left:22px;top:38px;width:100px;font-size:10px}
  .letterhead .contact{left:257px;top:26px;font-size:6.8px;line-height:8px;padding-left:8px;border-left:1px solid var(--rule)}
  .letterhead .contact .address{margin-bottom:4px}
  .letterhead .base-band{height:20px}
  .letter{position:absolute;left:42px;top:153px;width:308px;font-family:"Lato",sans-serif;font-weight:400;color:var(--text);font-size:6.3px;line-height:9.2px}
  .letter .recipient{margin-top:12px}
  .letter .recipient strong{font-weight:700}
  .letter .salutation{margin-top:18px}
  .letter .body p{margin-top:9px;text-align:justify}
  .letter .closing{margin-top:24px}
  .letter .signature{font-family:"Pinyon Script",cursive;font-size:14px;line-height:18px;margin-top:4px;margin-left:3px;color:var(--ink)}

  .letter-back{left:64px;top:249px;width:404px;height:539px}
  .letter-back .brand-mark{left:228px;top:500px;width:160px;font-size:10px}

  /* business cards */
  .card-front{left:543px;top:219px;width:185px;height:105px}
  .card-front .brand-mark{left:8px;top:38px;width:86px;font-size:6.4px}
  .card-front .contact{left:92px;top:26px;padding-left:8px;border-left:1px solid var(--ink);font-size:4px;line-height:5.3px}
  .card-front .name{font-weight:600;font-size:5.8px;line-height:6px;color:var(--ink)}
  .card-front .role{margin-bottom:5px}
  .card-front .address{margin-bottom:3px}
  .card-front .base-band{height:8px}
  .card-back{left:543px;top:343px;width:185px;height:105px}
  .card-back .brand-mark{left:0;top:40px;width:185px;font-size:9px}

  /* envelope */
  .envelope{left:752px;top:100px;width:248px;height:348px}
  .envelope .brand-mark{left:14px;top:250px;width:80px;font-size:7.6px}
  .envelope .contact{left:26px;top:305px;font-size:5.8px;line-height:7px}
  .envelope .base-band{height:14px}

  /* A5 cover */
  .cover{left:543px;top:462px;width:211px;height:326px}
  .cover .brand-mark{left:110px;top:254px;width:90px;font-size:7.6px}

  /* notepad */
  .notepad{left:788px;top:462px;width:211px;height:326px}
  .notepad .brand-mark{left:8px;top:16px;width:80px;font-size:6.6px}
  .notepad .web{position:absolute;right:19px;top:38px;font-family:"Montserrat",sans-serif;font-size:4px;color:var(--muted)}
  .notepad .base-band{height:12px}
  .writing-lines{position:absolute;left:19px;top:69px;width:172px;list-style:none}
  .writing-lines li{height:10px;border-bottom:.6px solid var(--rule)}

  /* poster sheet */
  .poster{left:1034px;top:195px;width:102px;height:589px;background:linear-gradient(90deg,#e2e2e2,#f2f2f2 45%,#d6d6d6)}
  .poster .brand-mark{left:0;top:52px;width:102px;font-size:7px}
  .poster .base-band{height:40px}
</style>
</head>
<body>
<div class="canvas">

  <svg width="0" height="0" style="position:absolute" aria-hidden="true">
    <symbol id="icon-phone" viewBox="0 0 10 10"><path d="M2 1h2l1 2.5-1.2.8a5 5 0 0 0 2 2l.8-1.2L9 6v2a1 1 0 0 1-1 1A7 7 0 0 1 1 2a1 1 0 0 1 1-1z"/></symbol>
    <symbol id="icon-fax" viewBox="0 0 10 10"><path d="M3 1h4v2H3zM1 4h8v4H7V6H3v2H1zM3 7h4v2H3z"/></symbol>
    <symbol id="icon-mail" viewBox="0 0 10 10"><path d="M1 2.5h8v5H1zM1.6 3l3.4 2.6L8.4 3" fill="none" stroke="currentColor"/><path d="M1 2.5h8v5H1z" fill-opacity=".25"/></symbol>
    <symbol id="icon-web" viewBox="0 0 10 10"><circle cx="5" cy="5" r="3.8" fill="none" stroke="#6d6d6d" stroke-width="1"/><path d="M1.2 5h7.6M5 1.2v7.6" stroke="#6d6d6d" stroke-width=".8"/></symbol>
  </svg>

  <!-- letterhead back sheet -->
  <section class="sheet dark letter-back">
    <div class="brand-mark on-dark"><span>Brightnest</span><span>Stays</span></div>
  </section>

  <!-- letterhead -->
  <section class="sheet paper letterhead">
    <div class="brand-mark"><span>Brightnest</span><span>Stays</span></div>
    <div class="contact">
      <div class="address"><p>Dummy State, Random Rd</p><p>City, PO 4000, Country</p></div>
      <p><svg class="icon"><use href="#icon-phone"/></svg>210.480.7100</p>
      <p><svg class="icon"><use href="#icon-fax"/></svg>310.620.9400</p>
      <p><svg class="icon" style="color:#6d6d6d"><use href="#icon-mail"/></svg>info@BrightnestStays.com</p>
      <p><svg class="icon"><use href="#icon-web"/></svg>www.BrightnestStays.com</p>
    </div>
    <article class="letter">
      <p class="date">01 January 2050</p>
      <div class="recipient">
        <p><strong>Company (Pvt) Ltd.</strong></p>
        <p>PO Box 3355 Mainville St</p>
        <p>Sample City Country 3355</p>
      </div>
      <p class="salutation">Dear Laura Fenwick,</p>
      <div class="body">
        <p>Lorem ipsum dolor sit amet, consectetuer adipiscing elit, sed diam nonummy nibh euismod tincidunt ut laoreet dolore magna aliquam erat volutpat. Ut wisi enim ad minim veniam, quis nostrud exerci tation ullamcorper suscipit lobortis nisl ut aliquip ex ea commodo consequat. Duis dolore te feugait nulla facilisi. Nam liber tempor cum soluta nobis eleifend option congue nihil imperdiet doming id quod mazim placerat facer possim assum. Lorem ipsum dolor sit amet, consectetuer adipiscing elit, sed diam nonummy nibh euismod tincidunt ut laoreet dolore magna aliquam erat volutpat. Ut wisi enim ad minim veniam, quis nostrud exerci tation ullamcorper suscipit lobortis nisl ut aliquip ex ea commodo consequat.</p>
        <p>Consectetuer adipiscing elit, sed diam nonummy nibh euismod tincidunt ut laoreet dolore magna aliquam erat volutpat. Ut wisi enim ad minim veniam, quis nostrud exerci tation ullamcorper suscipit lobortis nisl ut aliquip ex ea commodo consequat. Consectetuer adipiscing elit, sed diam nonummy nibh euismod tincidunt ut laoreet dolore magna aliquam erat volutpat. Ut wisi enim ad minim veniam, quis nostrud exerci tation ullamcorper suscipit lobortis nisl ut aliquip ex ea commodo consequat.</p>
        <p>Consectetuer adipiscing elit, sed diam nonummy nibh euismod tincidunt ut laoreet dolore magna aliquam erat volutpat. Ut wisi enim ad minim veniam, quis nostrud exerci tation ullamcorper suscipit lobortis nisl ut aliquip ex ea commodo consequat. Consectetuer adipiscing elit, sed diam nonummy nibh euismod tincidunt ut laoreet dolore magna aliquam erat volutpat. Ut wisi enim ad minim veniam, quis nostrud exerci tation ullamcorper suscipit lobortis nisl ut aliquip ex ea commodo consequat.</p>
      </div>
      <p class="closing">Sincerely Yours</p>
      <p class="signature">Marcus Elden Hale</p>
    </article>
    <div class="base-band"></div>
  </section>

  <!-- business card front -->
  <section class="sheet paper card-front">
    <div class="brand-mark"><span>Brightnest</span><span>Stays</span></div>
    <div class="contact">
      <p class="name">Owen Calder</p>
      <p class="role">Managing Director</p>
      <div class="address"><p>Dummy State, Random Rd</p><p>City, PO 4000, Country</p></div>
      <p><svg class="icon"><use href="#icon-phone"/></svg>210.480.7100</p>
      <p><svg class="icon"><use href="#icon-fax"/></svg>310.620.9400</p>
      <p><svg class="icon" style="color:#6d6d6d"><use href="#icon-mail"/></svg>info@BrightnestStays.com</p>
      <p><svg class="icon"><use href="#icon-web"/></svg>www.BrightnestStays.com</p>
    </div>
    <div class="base-band"></div>
  </section>

  <!-- business card back -->
  <section class="sheet dark card-back">
    <div class="brand-mark on-dark"><span>Brightnest</span><span>Stays</span></div>
  </section>

  <!-- envelope -->
  <section class="sheet paper envelope">
    <div class="brand-mark"><span>Brightnest</span><span>Stays</span></div>
    <div class="contact"><p>Dummy State, Random Rd</p><p>City, PO 4000, Country</p></div>
    <div class="base-band"></div>
  </section>

  <!-- A5 cover -->
  <section class="sheet dark cover">
    <div class="brand-mark on-dark"><span>Brightnest</span><span>Stays</span></div>
  </section>

  <!-- notepad -->
  <section class="sheet paper notepad">
    <div class="brand-mark"><span>Brightnest</span><span>Stays</span></div>
    <p class="web">www.BrightnestStays.com</p>
    <ul class="writing-lines">
      <li></li><li></li><li></li><li></li><li></li><li></li><li></li><li></li>
      <li></li><li></li><li></li><li></li><li></li><li></li><li></li><li></li>
      <li></li><li></li><li></li><li></li><li></li><li></li>
    </ul>
    <div class="base-band"></div>
  </section>

  <!-- poster sheet -->
  <section class="sheet poster">
    <div class="brand-mark"><span>Brightnest</span><span>Stays</span></div>
    <div class="base-band"></div>
  </section>

</div>
</body>
</html>
```